Marrowfield Contracting Business Cards

Front of card:

Full Logo
Name
Address
Office Phone
Cell Phone
Email
Website

Back:
Logo Mark in background
List and markets and services performed

```html
<!DOCTYPE html>
<html lang="en">
<head>
<meta charset="utf-8">
<title>Marrowfield Contracting Business Cards</title>
<link href="https://fonts.googleapis.com/css2?family=Lato:wght@400;700;900&display=swap" rel="stylesheet">
<style>
  :root {
    --stage: #2b2b2b;
    --card: #262626;
    --red: #e02127;
    --grey: #8a8a8a;
    --white: #f2f2f2;
    --muted: #c8c8c8;
  }
  * { margin: 0; padding: 0; box-sizing: border-box; }
  html, body { width: 1165px; height: 1200px; overflow: hidden; }
  body {
    background: var(--stage);
    font-family: "Lato", sans-serif;
    position: relative;
  }
  .card {
    position: absolute;
    width: 760px;
    height: 434px;
    background: var(--card);
    box-shadow: 0 18px 40px rgba(0,0,0,0.55);
    overflow: hidden;
  }
  .card--back { left: 60px; top: 110px; }
  .card--front { left: 345px; top: 650px; }

  .brand {
    display: flex;
    align-items: center;
    gap: 16px;
  }
  .brand__dot {
    width: 46px; height: 46px;
    border-radius: 50%;
    background: var(--grey);
    flex: none;
  }
  .brand__name {
    color: var(--red);
    font-weight: 900;
    text-transform: uppercase;
    letter-spacing: 2px;
    line-height: 1.05;
    font-size: 30px;
  }
  .card--back .brand { position: absolute; left: 150px; top: 176px; }

  .tagline {
    position: absolute;
    right: 60px;
    bottom: 62px;
    display: flex;
    align-items: center;
    gap: 8px;
    color: var(--muted);
    font-size: 13px;
    letter-spacing: 0.3px;
  }
  .tagline__mark { width: 7px; height: 7px; background: var(--red); }

  .card--front .brand {
    position: absolute;
    left: 70px; top: 160px;
    flex-direction: column;
    align-items: center;
    gap: 14px;
    text-align: center;
  }
  .card--front .brand__name { font-size: 26px; }

  .divider {
    position: absolute;
    left: 370px; top: 100px;
    width: 2px; height: 180px;
    background: linear-gradient(var(--red) 0 18%, var(--grey) 18% 82%, var(--red) 82% 100%);
  }

  .contact {
    position: absolute;
    left: 400px; top: 96px;
    color: var(--white);
    font-size: 16px;
    line-height: 1.3;
  }
  .contact__name { color: var(--red); font-weight: 900; font-size: 24px; line-height: 1.1; }
  .contact__role { margin-bottom: 10px; }
  .contact__address { margin-bottom: 10px; }
  .contact__list { list-style: none; }
  .contact__list li { display: flex; align-items: center; gap: 10px; }
  .contact__list svg { width: 13px; height: 13px; flex: none; }

  .accent-band {
    position: absolute;
    left: 0; right: 0; bottom: 0;
    height: 12px;
    background: var(--red);
  }
</style>
</head>
<body>
  <section class="card card--back">
    <div class="brand">
      <span class="brand__dot"></span>
      <span class="brand__name">Marrowfield<br>Contracting</span>
    </div>
    <p class="tagline"><span class="tagline__mark"></span>List and markets and services performed</p>
  </section>

  <section class="card card--front">
    <div class="brand">
      <span class="brand__dot"></span>
      <span class="brand__name">Marrowfield<br>Contracting</span>
    </div>

    <span class="divider"></span>

    <div class="contact">
      <p class="contact__name">Daniel Hartley</p>
      <p class="contact__role">Founder</p>
      <p class="contact__address">2408 Cedar Hollow Lane<br>Ridgeview 482, Northland</p>
      <ul class="contact__list">
        <li>
          <svg viewBox="0 0 12 12"><rect x="3" y="0.5" width="6" height="11" rx="1" fill="none" stroke="#e02127" stroke-width="1.3"/></svg>
          +112 555 0148
        </li>
        <li>
          <svg viewBox="0 0 12 12"><path d="M2 1l2.5 0 1 3-1.5 1c.8 1.5 1.5 2.2 3 3l1-1.5 3 1v2.5c-5 .5-9.5-4-9-9z" fill="#e02127"/></svg>
          +112 555 0148
        </li>
        <li>
          <svg viewBox="0 0 12 12"><rect x="0.5" y="2" width="11" height="8" fill="#e02127"/><path d="M0.5 2l5.5 4.5 5.5-4.5" fill="none" stroke="#262626" stroke-width="1"/></svg>
          hello@marrowfieldco.com
        </li>
        <li>
          <svg viewBox="0 0 12 12"><circle cx="6" cy="6" r="5.3" fill="none" stroke="#e02127" stroke-width="1.2"/><ellipse cx="6" cy="6" rx="2.2" ry="5.3" fill="none" stroke="#e02127" stroke-width="1"/><path d="M0.7 6h10.6" stroke="#e02127" stroke-width="1"/></svg>
          www.marrowfieldco.com
        </li>
      </ul>
    </div>

    <span class="accent-band"></span>
  </section>
</body>
</html>
```